Set of ads for a Medical Clinic in Costa Blanca Spain

We will start a small medical clinic for general medicine for Swedish and Scandinavians living on Costa Blanca Spain.
The clinic is called BrovaClinic
We need a set of ads with different sizes and also looking for a Designer to work with longtime.

Sizes of the adds:
One add with size 95 mm x 128 mm
One add with size 192 x 128 mm

We want one version of the add with a sign across the add "Öppnar i November" meaning "Opening in November" That add will be like a teaser and just creating attention to the clinic.

Skandinavisk Vårdcentral Costa Blanca

- Hembesök/Mobil Vårdcentral
- Lättakut
- Uppföljning av blodtryck, diabetes

Läs mer och boka din tid enkelt på www.brovaclinic-demo.com
Hitta hit:
Kliniken ligger utmed N332 vid Playa Flamenca, mitt emot Lorvista
Av. Tomás Herrera 7-2, 03412 Orihuela Costa

I have added pixelharbor images that could be used if you want, also open for other suggestions.

Target Market(s)

Swedish and Scandinavian patients looking for medical care in Spain

Industry/Entity Type

Medical

Colors
33b8a4
33a6d7
85cae6

Requirements
Must have
• Add in two sizes and versions.
• One add with size 95 mm x 128 mm
• One add with size 192 x 128 mm
• We want one add as a teaser before the clinic is opening. The add a bit faded and the text "Öppnar i November" across the add on the side. And one version of the add without "Öppnar i November"

```html
<!DOCTYPE html>
<html lang="sv">
<head>
<meta charset="utf-8">
<title>BrovaClinic – annonser</title>
<link rel="stylesheet" href="https://fonts.googleapis.com/css2?family=Open+Sans:wght@800&family=Source+Sans+3:wght@400;600&display=swap">
<style>
  :root {
    --teal: #33b8a4;
    --blue: #33a6d7;
    --panel-blue: #2ea3d6;
    --light-blue: #85cae6;
    --ink: #5b6770;
    --white: #ffffff;
    --backdrop: #ecebe8;
  }
  * { margin: 0; padding: 0; box-sizing: border-box; }
  html, body { width: 857px; height: 1200px; overflow: hidden; }
  body {
    position: relative;
    background: var(--backdrop);
    font-family: "Source Sans 3", "Myriad Pro", sans-serif;
  }
  .ad {
    position: absolute;
    left: 65px;
    width: 726px;
    height: 539px;
    background: var(--white);
    overflow: hidden;
    box-shadow: 0 3px 10px rgba(0,0,0,0.18);
  }
  .ad--teaser { top: 38px; }
  .ad--standard { top: 620px; }

  .ad__photo {
    position: absolute;
    left: 0; top: 0;
    width: 726px; height: 396px;
    overflow: hidden;
    background:
      radial-gradient(ellipse 120px 150px at 300px 230px, #e9c3b0 0%, rgba(233,195,176,0) 100%),
      radial-gradient(ellipse 140px 170px at 610px 200px, #d7b29f 0%, rgba(215,178,159,0) 100%),
      radial-gradient(ellipse 110px 110px at 220px 360px, #e7a9b5 0%, rgba(231,169,181,0) 100%),
      linear-gradient(90deg, #ddd8d2 0%, #cfc6be 45%, #e6e4e3 80%, #f1f2f4 100%);
  }
  .ad__photo-fade {
    position: absolute;
    left: 0; top: 0;
    width: 315px; height: 396px;
    background: linear-gradient(180deg, #ffffff 0%, #ffffff 28%, rgba(255,255,255,0.35) 60%, rgba(255,255,255,0) 100%);
  }

  .brand {
    position: absolute;
    left: 30px; top: 34px;
  }
  .brand__name {
    font-family: "Source Sans 3", sans-serif;
    font-weight: 600;
    font-size: 46px;
    line-height: 1;
    color: var(--ink);
    letter-spacing: -0.5px;
  }
  .brand__tagline {
    margin-top: 2px;
    font-size: 17.5px;
    font-weight: 400;
    color: var(--blue);
  }

  .headline {
    position: absolute;
    font-family: "Open Sans", sans-serif;
    font-weight: 800;
    line-height: 1;
    white-space: nowrap;
    letter-spacing: -1px;
  }
  .headline--white { color: var(--white); }
  .headline--blue { color: var(--panel-blue); }

  .ad--teaser .headline--white { left: 24px; top: 331px; font-size: 70px; letter-spacing: -2.5px; }
  .ad--teaser .headline--blue { left: 318px; top: 325px; font-size: 76px; }

  .ad--standard .headline--white { left: 26px; font-size: 44px; letter-spacing: -1.5px; }
  .ad--standard .headline--white.line-1 { top: 306px; }
  .ad--standard .headline--white.line-2 { top: 354px; }
  .ad--standard .headline--blue { left: 318px; top: 336px; font-size: 66px; }

  .services {
    position: absolute;
    left: 27px; top: 405px;
    width: 290px;
    list-style: none;
    font-size: 20.5px;
    line-height: 26px;
    color: var(--panel-blue);
  }
  .services li {
    position: relative;
    padding-left: 15px;
  }
  .services li::before {
    content: "";
    position: absolute;
    left: 0; top: 8px;
    width: 11px; height: 11px;
    border-radius: 50%;
    background: var(--teal);
  }

  .info-panel {
    position: absolute;
    left: 315px; top: 396px;
    width: 411px; height: 143px;
    background: var(--panel-blue);
    color: var(--white);
    padding: 10px 0 0 23px;
    font-size: 18px;
    line-height: 22px;
  }
  .info-panel strong { font-weight: 600; }
  .info-panel .booking { margin-bottom: 9px; }
</style>
</head>
<body>

<section class="ad ad--teaser">
  <div class="ad__photo" role="img" aria-label="Foto: läkare undersöker ett leende barn i mammans famn på en ljus mottagning">
    <div class="ad__photo-fade"></div>
    <div class="headline headline--white">Öppnar i</div>
    <div class="headline headline--blue">November</div>
  </div>
  <div class="brand">
    <div class="brand__name">BrovaClinic</div>
    <div class="brand__tagline">Skandinavisk Läkarmottagning</div>
  </div>
  <ul class="services">
    <li>Hembesök/Mobil Vårdcentral</li>
    <li>Lättakut</li>
    <li>Uppföljning av blodtryck,<br>diabetes</li>
  </ul>
  <div class="info-panel">
    <p class="booking"><strong>Läs mer och boka din tid enkelt på</strong><br>www.brovaclinic-demo.com</p>
    <p><strong>Hitta hit:</strong> Kliniken ligger utmed N332<br>vid Playa Flamenca, mitt emot Lorvista<br>Av. Tomás Herrera 7-2, 03412 Orihuela Costa</p>
  </div>
</section>

<section class="ad ad--standard">
  <div class="ad__photo" role="img" aria-label="Foto: läkare undersöker ett leende barn i mammans famn på en ljus mottagning">
    <div class="ad__photo-fade"></div>
    <div class="headline headline--white line-1">Skandinavisk</div>
    <div class="headline headline--white line-2">Vårdcentral</div>
    <div class="headline headline--blue">Costa Blanca</div>
  </div>
  <div class="brand">
    <div class="brand__name">BrovaClinic</div>
    <div class="brand__tagline">Skandinavisk Läkarmottagning</div>
  </div>
  <ul class="services">
    <li>Hembesök/Mobil Vårdcentral</li>
    <li>Lättakut</li>
    <li>Uppföljning av blodtryck,<br>diabetes</li>
  </ul>
  <div class="info-panel">
    <p class="booking"><strong>Läs mer och boka din tid enkelt på</strong><br>www.brovaclinic-demo.com</p>
    <p><strong>Hitta hit:</strong> Kliniken ligger utmed N332<br>vid Playa Flamenca, mitt emot Lorvista<br>Av. Tomás Herrera 7-2, 03412 Orihuela Costa</p>
  </div>
</section>

</body>
</html>
```